Design Website Templates for Photographers for Lumora Inc. (bookwrenlyte.example)

Lumora Inc. is a generative website company for wedding photographers.
We are seeking new photography website design inspirations for the next template to be offered on our platform. The catch is you must use the same data for your designs. You also must use all of the data somewhere in the design. You cannot add new content besides the data available. If you wish to add any elements It will be hardcoded and must be universally fitting for many different photographers. We recommend not using any hardcoded test.
Don't be afraid to be creative! Although the most important element of a photographers website is the photos, we are looking for unique and out-of-the-box designs for the actual site as well.
Here is the User generated data available to you:
- 4 Hero Images Landscape, 4 Hero Images Portrait
- Tagline “destination photographer based in Maui, Hawaii”
- “About Photo” of the photographer
- “About” Biography Text
- The design can use up to 3 colors + background color and 2 fonts
- 9 Gallery images
- 3 Packages/services that include landscape/portrait images, a price, a title and text
- Testimonials made up of an image, text and text for the name of testimonial giver
See some examples of our current website designs attached. You can use any of the data you see in the designs.
Updates
We are looking for designs that are less feminine and are more neutral in color and fonts. Currently our templates are more oriented towards feminine photographers. We want to have designs that speak to diverse audiences. We thank everyone for submitting and are reviewing the designs.
Number of Pages Required
1 page
Look and feel
Each slider illustrates characteristics of the customer's brand and the style your logo design should communicate.

```html
<!DOCTYPE html>
<html lang="en">
<head>
<meta charset="utf-8">
<title>Lumora Inc. — Destination Photographer</title>
<link rel="stylesheet" href="https://fonts.googleapis.com/css2?family=Cinzel:wght@400;500&family=Poppins:ital,wght@0,400;0,500;1,500&display=swap">
<style>
:root{
  --ink:#1d1d1d;
  --muted:#5a5a5a;
  --line:#3a3a3a;
  --paper:#ffffff;
  --mist:#f4f4f4;
  --night:#1f2226;
  --white:#ffffff;
}
*{margin:0;padding:0;box-sizing:border-box}
html,body{width:1200px;height:4317px;overflow:hidden}
body{position:relative;background:var(--paper);font-family:"Poppins",sans-serif;color:var(--ink)}
.abs{position:absolute}
.serif{font-family:"Cinzel",serif;font-weight:400}
.photo{position:absolute}

/* hero */
.hero{left:0;top:0;width:1200px;height:747px;background:linear-gradient(180deg,#2f5a32 0%,#3d6b3a 28%,#9fb0a6 40%,#c9d2cf 55%,#d7ddd9 75%,#5d7d3a 92%,#3f6a2a 100%)}
.hero-panel{left:0;top:377px;width:838px;height:288px;background:rgba(255,255,255,.55);clip-path:polygon(0 0,100% 0,77% 100%,0 100%)}
.logo{left:85px;top:46px;font-size:34px;color:var(--white);letter-spacing:.5px}
.nav a{position:absolute;top:58px;font-size:15px;color:var(--white);text-decoration:none}
.btn-nav{left:949px;top:42px;width:167px;height:54px;border:1.5px solid var(--white);color:var(--white);font-size:15px;display:flex;align-items:center;justify-content:center}
.hero-title{left:85px;top:425px;font-size:44px;line-height:52px;color:var(--ink);font-weight:500}
.btn-hero{left:85px;top:558px;width:244px;height:74px;border:2px solid var(--line);font-size:19px;display:flex;align-items:center;justify-content:center;color:var(--ink)}
.dot{top:696px;width:16px;height:16px;border-radius:50%;background:var(--white)}

/* about */
.frame{position:absolute;border:2px solid var(--line)}
.about-title{left:613px;top:876px;font-size:33px}
.about-text{left:613px;top:959px;width:503px;font-size:15px;line-height:30.7px;text-align:justify;color:var(--ink)}
.btn-outline{border:2px solid var(--line);display:flex;align-items:center;justify-content:center;font-size:15px;color:var(--ink)}

/* sections */
.section-title{left:0;width:1200px;text-align:center;font-size:36px}
.mist{left:0;top:2809px;width:1200px;height:652px;background:var(--mist)}
.card{position:absolute;top:2975px;width:326px;height:394px;background:var(--paper)}
.card .photo{left:6px;top:6px;width:314px;height:242px}
.price{position:absolute;left:18px;top:185px;height:38px;padding:0 16px;background:var(--paper);font-size:15px;display:flex;align-items:center}
.card h3{position:absolute;left:18px;top:272px;font-size:21px;font-weight:500;color:#3b3b3b}
.card p{position:absolute;left:18px;top:313px;width:300px;font-size:15px;line-height:20px;color:var(--muted)}

/* testimonials */
.testimonials{left:0;top:3461px;width:1200px;height:489px;background:linear-gradient(180deg,#2b2e33 0%,#1c1e22 55%,#15171a 100%)}
.quote{position:absolute;top:3663px;width:332px;font-size:16px;line-height:26px;color:var(--white);text-align:justify}
.quote-mark{position:absolute;font-family:"Cinzel",serif;font-size:34px;color:var(--white)}
.quote-name{position:absolute;top:3812px;font-size:16px;font-style:italic;font-weight:500;color:var(--white)}

/* footer */
.footer{left:0;top:3950px;width:1200px;height:367px;background:var(--mist)}
.foot-link{position:absolute;top:4142px;font-size:15px;color:var(--ink)}
.rule{left:85px;top:4230px;width:1031px;height:1.5px;background:var(--line)}
.social{position:absolute;top:4249px;width:34px;height:34px;border-radius:50%;border:1.5px solid var(--ink)}
</style>
</head>
<body>

<!-- hero -->
<div class="abs hero" role="img" aria-label="Bride in a flowing white gown and groom holding a bouquet beside a lake with forested hills"></div>
<div class="abs hero-panel"></div>
<div class="abs logo serif">Lumora Inc.</div>
<nav class="nav">
  <a style="left:637px">About</a>
  <a style="left:724px">Testimonials</a>
  <a style="left:863px">Portfolio</a>
</nav>
<div class="abs btn-nav">Book Now</div>
<h1 class="abs hero-title serif">Destination Photographer<br>based in Maui, Hawaii</h1>
<div class="abs btn-hero">BOOK NOW</div>
<div class="abs dot" style="left:106px"></div>
<div class="abs dot" style="left:124px;background:#2a2a1a"></div>
<div class="abs dot" style="left:143px"></div>
<div class="abs dot" style="left:163px"></div>

<!-- about -->
<div class="frame" style="left:129px;top:836px;width:277px;height:310px"></div>
<div class="frame" style="left:196px;top:1000px;width:277px;height:311px"></div>
<div class="photo" style="left:85px;top:944px;width:249px;height:321px;background:linear-gradient(160deg,#5b6258,#2b2d2b 60%,#1c1c1c)" role="img" aria-label="Photographer holding a camera to the eye"></div>
<div class="photo" style="left:275px;top:880px;width:252px;height:325px;background:var(--paper)"></div>
<div class="photo" style="left:277px;top:882px;width:248px;height:321px;background:linear-gradient(170deg,#5a5c5c,#2e3030 55%,#4a4a48)" role="img" aria-label="Camera mounted on a gimbal stabiliser"></div>
<h2 class="abs about-title serif">About Lumora Inc.</h2>
<p class="abs about-text">Lorem ipsum dolor sit amet, consectetur adipiscing elit, sed do eiusmod tempor incididunt ut labore et dolore magna aliqua. Ut enim ad minim veniam, quis nostrud exercitation ullamco laboris nisi ut aliquip ex ea commodo consequat. Duis aute irure dolor in reprehenderit in voluptate velit esse cillum dolore eu fugiat nulla pariatur. Excepteur sint occaecat cupidatat non proident, sunt in culpa qui officia .</p>
<div class="abs btn-outline" style="left:613px;top:1205px;width:145px;height:64px">Read More</div>

<!-- portfolio -->
<h2 class="abs section-title serif" style="top:1437px">Portfolio</h2>
<div class="photo" style="left:87px;top:1547px;width:505px;height:292px;background:linear-gradient(135deg,#7d6a3a,#a58a4e 45%,#3a3a2e)" role="img" aria-label="Couple dancing in an autumn field"></div>
<div class="photo" style="left:608px;top:1547px;width:505px;height:292px;background:linear-gradient(180deg,#6d8a64,#5f7f3f 60%,#7a9a4a)" role="img" aria-label="Couple standing on a lawn among pine trees"></div>
<div class="photo" style="left:85px;top:1854px;width:336px;height:293px;background:radial-gradient(circle at 55% 55%,#a2402e,#6b3a20 50%,#b88a5a)" role="img" aria-label="Bride in a red veil framed by a blurred foreground"></div>
<div class="photo" style="left:436px;top:1854px;width:333px;height:293px;background:linear-gradient(135deg,#2f5f5c,#6a5848 55%,#3a6a68)" role="img" aria-label="Couple on rocks above sea waves"></div>
<div class="photo" style="left:783px;top:1854px;width:333px;height:293px;background:linear-gradient(135deg,#c0302a,#8a3a22 50%,#c49a4a)" role="img" aria-label="Hands with henna and gold bangles"></div>
<div class="photo" style="left:87px;top:2160px;width:505px;height:292px;background:linear-gradient(180deg,#3e6aa6,#d49a4a 55%,#3a3e48)" role="img" aria-label="Couple in front of a glass pyramid at sunset"></div>
<div class="photo" style="left:608px;top:2160px;width:505px;height:292px;background:linear-gradient(180deg,#8aa4c4,#e4c49a 55%,#a58e70)" role="img" aria-label="Couple dancing on a beach at sunset"></div>
<div class="photo" style="left:85px;top:2469px;width:654px;height:238px;background:linear-gradient(100deg,#5a4030,#8a5a3a 40%,#3a5a7a)" role="img" aria-label="Henna-covered hands with bangles"></div>
<div class="photo" style="left:756px;top:2469px;width:359px;height:238px;background:linear-gradient(90deg,#3a2a24,#8a3a3a 50%,#b8b0a0)" role="img" aria-label="Bride in a red sari beside a window"></div>

<!-- packages -->
<div class="abs mist"></div>
<h2 class="abs section-title serif" style="top:2881px">Featured Packages</h2>
<div class="card" style="left:85px">
  <div class="photo" style="background:linear-gradient(135deg,#2f6a4a,#b8505a 60%,#d4a44a)" role="img" aria-label="Bride in traditional jewellery"></div>
  <div class="price">$ 1250 CAD</div>
  <h3>Lorem ipsum dolor sit amet</h3>
  <p>Lorem ipsum dolor sit amet, consectetur adipiscing elit, sed do eiusmod</p>
</div>
<div class="card" style="left:437px">
  <div class="photo" style="background:linear-gradient(160deg,#2f4a2a,#6a7a3a 50%,#d8d4c8)" role="img" aria-label="Couple walking along a garden path"></div>
  <div class="price">$ 1300 CAD</div>
  <h3>Lorem ipsum dolor sit amet</h3>
  <p>Lorem ipsum dolor sit amet, consectetur adipiscing elit, sed do eiusmod</p>
</div>
<div class="card" style="left:784px">
  <div class="photo" style="background:linear-gradient(180deg,#e8c27a,#c49a4a 50%,#6a6a2a)" role="img" aria-label="Couple in a golden field at sunset"></div>
  <div class="price">$ 1350CAD</div>
  <h3>Lorem ipsum dolor sit amet</h3>
  <p>Lorem ipsum dolor sit amet, consectetur adipiscing elit, sed do eiusmod</p>
</div>

<!-- testimonials -->
<div class="abs testimonials" role="img" aria-label="Couple silhouetted against a dusk sky by the water"></div>
<h2 class="abs section-title serif" style="top:3538px;color:var(--white)">Testimonials</h2>
<svg class="abs" style="left:84px;top:3725px" width="24" height="34" viewBox="0 0 24 34"><path d="M18 3 L5 17 L18 31" fill="none" stroke="#fff" stroke-width="4"/></svg>
<svg class="abs" style="left:1092px;top:3725px" width="24" height="34" viewBox="0 0 24 34"><path d="M6 3 L19 17 L6 31" fill="none" stroke="#fff" stroke-width="4"/></svg>

<span class="quote-mark" style="left:174px;top:3628px">“</span>
<p class="quote" style="left:193px">Lorem ipsum, or lipsum as it is sometimes known, is dummy text used in laying out print, graphic or web designs. The passage is attributed to an unknown typesetter in the 15th century</p>
<span class="quote-mark" style="left:318px;top:3760px">”</span>
<span class="quote-name" style="left:193px">Lorem ipsum dolor</span>

<span class="quote-mark" style="left:676px;top:3628px">“</span>
<p class="quote" style="left:696px">Lorem ipsum, or lipsum as it is sometimes known, is dummy text used in laying out print, graphic or web designs. The passage is attributed to an unknown typesetter in the 15th century</p>
<span class="quote-mark" style="left:820px;top:3760px">”</span>
<span class="quote-name" style="left:696px">Lorem ipsum dolor</span>

<!-- footer -->
<footer class="abs footer"></footer>
<div class="abs serif" style="left:0;top:4018px;width:1200px;text-align:center;font-size:34px">Lumora Inc.</div>
<span class="foot-link" style="left:201px">ABOUT</span>
<span class="foot-link" style="left:288px">BLOG</span>
<span class="foot-link" style="left:365px">TESTIMONIALS</span>
<div class="abs btn-outline" style="left:524px;top:4120px;width:174px;height:67px">BOOK NOW</div>
<span class="foot-link" style="left:768px">PORTFOLIO</span>
<span class="foot-link" style="left:885px">GET IN TOUCH</span>
<div class="abs rule"></div>
<div class="abs" style="left:85px;top:4257px;font-size:14px">Copyright © 2023 All Rights Reserved By Companyname</div>
<span class="social" style="left:965px;background:var(--ink)"></span>
<span class="social" style="left:1003px"></span>
<span class="social" style="left:1042px"></span>
<span class="social" style="left:1080px"></span>

</body>
</html>
```